Brochure to attract insurance agents to outsource their bookkeeping

I need a brochure to handout at trade shows. Company name is Marrowfield Tally & Ledger Services. We go by MTLS. We provide bookkeeping services. I have attached the current brochure, which is a few years old, stale and outdated (not created on ArtQuorra). I have also attached our graphic identity manual which show fonts/colors as well as our logo in 3 styles

Target Market(s)

Insurance Agents needing bookkeeping services

Industry/Entity Type

Accounting

Other font styles liked:
• See the graphic id manual

Colors
00AB8E
00BBA5
67D7C9
C6EFE9
E9F9F6

Requirements
Must have
• Services noted (see current brochure), contact info, reference to Velmont Orbis

```html
<!DOCTYPE html>
<html lang="en">
<head>
<meta charset="utf-8">
<title>Marrowfield Tally &amp; Ledger Services – Brochure</title>
<link rel="stylesheet" href="https://fonts.googleapis.com/css2?family=Montserrat:wght@700;800&family=PT+Sans+Narrow&family=Roboto:wght@700&display=swap">
<style>
  :root{
    --teal-deep:#00AB8E;
    --teal:#1FB196;
    --teal-bright:#00BBA5;
    --teal-soft:#67D7C9;
    --mint:#C6EFE9;
    --mint-pale:#E9F9F6;
    --white:#FFFFFF;
  }
  *{margin:0;padding:0;box-sizing:border-box}
  html,body{width:848px;height:1200px;overflow:hidden;background:var(--teal)}
  .brochure{
    position:relative;width:848px;height:1200px;overflow:hidden;
    background:
      radial-gradient(ellipse 520px 380px at 120px 1000px, rgba(103,215,201,.45), transparent 70%),
      radial-gradient(ellipse 420px 600px at 760px 80px, rgba(103,215,201,.35), transparent 70%),
      radial-gradient(ellipse 300px 500px at 330px 1120px, rgba(198,239,233,.35), transparent 70%),
      linear-gradient(160deg, #3CC1A9 0%, #1FB196 45%, #2DBAA0 100%);
    font-family:"Montserrat",sans-serif;
  }
  .masthead-band{position:absolute;left:0;top:0;width:478px;height:102px}
  .brand{
    position:absolute;left:28px;top:14px;height:74px;
    display:flex;align-items:center;gap:12px;
    color:var(--teal-deep);font-weight:800;text-transform:uppercase;
  }
  .brand-name{width:190px;font-size:15px;line-height:1.15}
  .brand-short{font-size:64px;line-height:1;letter-spacing:-1px}
  .headline{
    position:absolute;left:10px;top:200px;width:478px;
    color:var(--mint);font-weight:700;text-align:center;
    font-size:36px;line-height:36px;letter-spacing:.5px;white-space:nowrap;
  }
  .headline span{display:block}
  .headline .line-1{margin-bottom:38px}
  .headline .line-2{margin-bottom:22px}
  .headline .line-3{margin-bottom:24px}
  .step-pattern{position:absolute;left:18px;top:516px}
  .platform-note{
    position:absolute;left:18px;top:594px;width:440px;text-align:center;
    font-family:"PT Sans Narrow",sans-serif;font-size:21px;color:var(--mint-pale);letter-spacing:.3px;
  }
  .portrait-frame{position:absolute;left:483px;top:134px}
  .services-title{
    position:absolute;left:20px;top:693px;
    color:var(--mint-pale);font-weight:700;font-size:40px;letter-spacing:.5px;
  }
  .services{
    position:absolute;left:38px;top:775px;list-style:none;
    font-family:"PT Sans Narrow",sans-serif;font-size:28.5px;color:var(--mint-pale);
  }
  .services li{display:flex;align-items:center;height:51.4px;white-space:nowrap}
  .services li::before{
    content:"";width:17px;height:17px;border-radius:50%;background:var(--white);margin-right:13px;flex:none;
  }
  .ornament-area{
    position:absolute;right:0;top:690px;width:270px;height:510px;
    background:radial-gradient(ellipse at 65% 55%, rgba(233,249,246,.35), rgba(233,249,246,0) 70%);
  }
  .contact{position:absolute;left:208px;top:1146px;width:410px;height:54px}
  .contact-lines{
    position:absolute;left:0;top:1147px;width:848px;
    font-family:"Roboto",sans-serif;font-weight:700;color:var(--teal-deep);font-size:15.5px;
  }
  .contact-phone,.contact-web{position:absolute;display:flex;align-items:center;gap:8px;white-space:nowrap}
  .contact-phone{left:345px;top:6px}
  .contact-web{left:256px;top:28px;font-size:16.5px}
</style>
</head>
<body>
<main class="brochure">
  <svg class="masthead-band" viewBox="0 0 478 102" aria-hidden="true">
    <polygon points="0,0 408,0 478,102 0,102" fill="#C6EFE9"/>
  </svg>
  <div class="brand">
    <span class="brand-name">Marrowfield Tally &amp; Ledger Services</span>
    <span class="brand-short">MTLS</span>
  </div>

  <h1 class="headline">
    <span class="line-1">MARROWFIELD TALLY</span>
    <span class="line-2">&amp;</span>
    <span class="line-3">LEDGER</span>
    <span class="line-4">SERVICES</span>
  </h1>

  <svg class="step-pattern" width="440" height="62" viewBox="0 0 440 62" aria-hidden="true">
    <g fill="#C6EFE9" stroke="#9FD9CE" stroke-width="1">
      <rect x="0" y="18" width="40" height="38"/>
      <rect x="41" y="1" width="40" height="38"/>
      <rect x="72" y="18" width="40" height="38"/>
      <rect x="113" y="1" width="40" height="38"/>
      <rect x="143" y="18" width="40" height="38"/>
      <rect x="184" y="1" width="40" height="38"/>
      <rect x="214" y="18" width="40" height="38"/>
      <rect x="255" y="1" width="40" height="38"/>
      <rect x="286" y="18" width="40" height="38"/>
      <rect x="326" y="1" width="40" height="38"/>
      <rect x="357" y="20" width="40" height="39"/>
      <rect x="398" y="3" width="40" height="38"/>
    </g>
  </svg>
  <p class="platform-note">Velmont Orbis bookkeeping specialists</p>

  <svg class="portrait-frame" width="352" height="622" viewBox="0 0 352 622">
    <defs>
      <linearGradient id="portraitTone" x1="0" y1="0" x2="0" y2="1">
        <stop offset="0" stop-color="#C6EFE9"/>
        <stop offset=".45" stop-color="#8C8A86"/>
        <stop offset="1" stop-color="#1C1C1E"/>
      </linearGradient>
    </defs>
    <path d="M22,20 H348 V420 Q348,620 150,620 H22" fill="none" stroke="#C6EFE9" stroke-width="4"/>
    <path d="M30,30 H340 V418 Q340,606 150,606 H30" fill="none" stroke="#C6EFE9" stroke-width="3"/>
    <g role="img" aria-label="Portrait photo of a smiling businesswoman in a dark suit holding a tablet">
      <path d="M0,600 V140 Q0,1 140,1 H330 V420 Q330,600 150,600 Z" fill="url(#portraitTone)"/>
    </g>
  </svg>

  <h2 class="services-title">OUR SERVICES:</h2>
  <ul class="services">
    <li>RECONCILE &amp; PAY AGENCY BILL PREMIUMS</li>
    <li>RECORD DIRECT BILL COMMISSION</li>
    <li>PREPARE &amp; INTERPRET FINANCIAL STATEMENTS</li>
    <li>RECONCILE GENERAL LEDGER ACCOUNTS</li>
    <li>RECONCILE CUSTOMER ACCOUNTS RECEIVABLE</li>
    <li>PAY VENDOR INVOICES</li>
    <li>PROCESS PAYROLL</li>
  </ul>

  <div class="ornament-area" role="img" aria-label="Decorative black and silver floral swirl ornament"></div>

  <svg class="contact" viewBox="0 0 410 54" aria-hidden="true">
    <polygon points="26,0 372,0 410,54 0,54" fill="#FFFFFF"/>
  </svg>
  <div class="contact-lines">
    <div class="contact-phone">
      <svg width="18" height="18" viewBox="0 0 24 24" aria-hidden="true"><path fill="#00AB8E" d="M6.6 10.8a15.1 15.1 0 0 0 6.6 6.6l2.2-2.2a1 1 0 0 1 1-.25 11.4 11.4 0 0 0 3.6.57 1 1 0 0 1 1 1V20a1 1 0 0 1-1 1A17 17 0 0 1 3 4a1 1 0 0 1 1-1h3.5a1 1 0 0 1 1 1c0 1.250.2 2.45.57 3.57a1 1 0 0 1-.25 1z"/></svg>
      <span>555.014.2290</span>
    </div>
    <div class="contact-web">
      <svg width="20" height="14" viewBox="0 0 20 14" aria-hidden="true"><rect x="1" y="1" width="18" height="12" fill="none" stroke="#00AB8E" stroke-width="1.4"/><path d="M1 1l9 7 9-7M1 13l7-6M19 13l-7-6" fill="none" stroke="#00AB8E" stroke-width="1.4"/></svg>
      <span>WWW.MarrowfieldTally.com</span>
    </div>
  </div>
</main>
</body>
</html>
```